Infographic from a blog post about Reliability Centred Maintenance (RCM)

I need someone to convert a detailed blog post into an Infographic. The post is here: https://www.gearmontlabs.com/reliability-centered-maintenance-principles/

The infographic should include:
(1) the history of RCM, probably best done by using the 1st, 2nd and 3rd generation of maintenance concepts as discussed in the article. For the 3rd generation includesome of the metrics that show the difference RCM made e.g. the comparison between the maintenance of a QX-7 versus that of the 583-240

(2) All the 9 principles that are mentioned in the article with a large part of the infographic dedicated to Principle #2 with the failure patterns and distributions

For the infographic make sure it fits with the design & branding of the overall site www.gearmontlabs.com

Industry/Entity Type

Industrial

Font styles to use
Other font styles liked:
• roboto condensed bold for titles, raleway for text

Colors
0292cd
333333
ffc214

Requirements
Must have
• The infographic must include:
• (1) the history of RCM and some of the metrics that show the difference RCM made e.g. the comparison between the maintenance of a QX-7 versus that of the 583-240
• (2) All the 9 principles that are mentioned in the article with a large part of the infographic dedicated to Principle #2 with the failure patterns and distributions
• Use following main colours:
• #3C3C3C
• #0187AC
• Use the following colors for highlights:
• #079F6D
• #B91449
• #FFC000
Nice to have
• For the history section use some imagery along these lines:
• 1st generation of maintenance = industrial revolution so steam train, steam equipment
• 2nd generation of maintenance = from world war 2, maybe show a tank
• 3rd generation of maintenance = developed by aviation so show a picture of a 583-240 airplane

```html
<!DOCTYPE html>
<html lang="en">
<head>
<meta charset="utf-8">
<title>Reliability Centered Maintenance – 9 Principles of Modern Maintenance</title>
<link href="https://fonts.googleapis.com/css2?family=Roboto+Condensed:wght@400;700&family=Raleway:wght@400;500;600;700&display=swap" rel="stylesheet">
<style>
:root{
  --ink:#3c3c3c;
  --ink-soft:#5a5a5a;
  --brand:#0187ac;
  --brand-deep:#1b5d86;
  --brand-light:#dcedf5;
  --header:#1b8fb8;
  --accent:#ffc000;
  --red:#b91449;
  --green:#079f6d;
  --band:#eef1f3;
  --rule:#c9d3da;
  --white:#ffffff;
}
*{box-sizing:border-box;margin:0;padding:0}
html,body{width:1200px;height:5164px;overflow:hidden;background:var(--white)}
body{font-family:"Raleway",sans-serif;color:var(--ink);position:relative}
.abs{position:absolute}

/* header */
.masthead{position:absolute;left:0;top:0;width:1200px;height:320px;background:var(--header);overflow:hidden}
.masthead svg{position:absolute;left:0;top:0}
.brand{position:absolute;left:40px;top:40px;display:flex;align-items:center;gap:12px;color:var(--white);font-family:"Raleway",sans-serif;font-weight:700;font-size:22px}
.brand-dot{width:30px;height:30px;border-radius:50%;background:var(--white)}
.title{position:absolute;left:260px;top:34px;color:var(--white);font-family:"Roboto Condensed",sans-serif;font-weight:700;font-size:62px;line-height:60px}
.subtitle{position:absolute;left:260px;top:232px;color:#d9f0fa;font-family:"Roboto Condensed",sans-serif;font-weight:400;font-size:30px;letter-spacing:2px}

/* section headings */
.section-title{position:absolute;left:60px;display:flex;align-items:center;gap:16px;font-family:"Roboto Condensed",sans-serif;font-weight:700;font-size:38px;color:var(--brand-deep)}
.section-title::before{content:"";width:22px;height:22px;background:var(--brand)}
.section-rule{position:absolute;left:60px;width:1080px;height:2px;background:var(--rule)}

/* generations */
.gen{position:absolute;top:390px;width:300px;text-align:center}
.gen-label{font-size:28px;line-height:34px;color:var(--brand-deep);font-family:"Roboto Condensed",sans-serif}
.gen-label sup{font-size:16px}
.gen-box{margin:14px auto 12px;width:230px;height:90px;background:var(--brand);color:var(--white);display:flex;align-items:center;justify-content:center;font-family:"Roboto Condensed",sans-serif;font-weight:700;font-size:26px;line-height:30px}
.gen-text{font-size:19px;line-height:25px;color:var(--ink-soft)}
.gen-link{position:absolute;top:483px;height:2px;background:var(--brand)}

/* timeline */
.spine{position:absolute;left:599px;top:720px;width:3px;height:600px;background:var(--rule)}
.event{position:absolute;width:420px}
.event.left{left:130px;text-align:right}
.event.right{left:650px}
.event .year{font-family:"Roboto Condensed",sans-serif;font-weight:700;font-size:42px;color:var(--brand);line-height:44px}
.event p{font-size:17px;line-height:23px;color:var(--ink-soft);margin-top:4px}
.node{position:absolute;left:590px;width:22px;height:22px;border-radius:50%;background:var(--white);border:5px solid var(--brand)}

/* comparison band */
.compare{position:absolute;left:0;top:1345px;width:1200px;height:475px;background:var(--band)}
.compare .lead{position:absolute;left:100px;width:1000px;text-align:center;font-size:23px;line-height:31px;color:var(--ink);font-weight:600}
.plane-box{position:absolute;top:90px;width:420px;height:200px;background:var(--white);border-top:6px solid var(--brand);text-align:center;padding:20px 30px}
.plane-box h3{font-family:"Roboto Condensed",sans-serif;font-weight:700;font-size:56px;color:var(--brand-deep);line-height:58px}
.plane-box p{font-size:17px;line-height:23px;color:var(--ink-soft);margin-top:8px}
.vs{position:absolute;left:555px;top:150px;width:90px;height:90px;border-radius:50%;background:var(--brand-deep);color:var(--white);font-family:"Roboto Condensed",sans-serif;font-weight:700;font-size:36px;display:flex;align-items:center;justify-content:center}

/* principles wheel */
.wheel{position:absolute;left:0;top:1840px;width:1200px;height:460px}
.tag{position:absolute;display:flex;align-items:center;gap:12px;font-size:20px;line-height:24px;color:var(--ink);font-weight:600}
.tag .num{font-family:"Roboto Condensed",sans-serif;font-weight:700;font-size:44px;color:var(--brand)}
.tag.left{right:760px;text-align:right;justify-content:flex-end}
.tag.right{left:760px}
.hub{position:absolute;left:470px;top:100px;width:260px;height:260px;text-align:center;display:flex;align-items:center;justify-content:center;font-family:"Roboto Condensed",sans-serif;font-weight:700;font-size:34px;line-height:38px;color:var(--brand-deep)}

/* principle details */
.detail{position:absolute;width:500px}
.detail h4{display:flex;gap:12px;align-items:flex-start;font-family:"Roboto Condensed",sans-serif;font-weight:700;font-size:25px;line-height:28px;color:var(--brand-deep)}
.detail h4 span{font-size:46px;line-height:40px;color:var(--red)}
.detail p{font-size:15px;line-height:20px;color:var(--ink-soft);margin:6px 0 0 66px}

/* table */
.footnote{position:absolute;left:80px;top:3205px;font-size:19px;color:var(--ink-soft)}
.table-title{position:absolute;left:0;top:3245px;width:1200px;text-align:center;font-family:"Roboto Condensed",sans-serif;font-weight:700;font-size:46px;color:var(--brand-deep)}
.patterns{position:absolute;left:80px;top:3320px;width:1040px;border-collapse:collapse;table-layout:fixed}
.patterns th,.patterns td{border:2px solid var(--rule);text-align:center;vertical-align:middle}
.patterns thead th{background:var(--white);font-family:"Roboto Condensed",sans-serif;font-weight:700;font-size:26px;color:var(--brand-deep);height:50px}
.patterns thead tr.src th{font-family:"Raleway",sans-serif;font-weight:500;font-size:15px;line-height:18px;color:var(--ink-soft)}
.patterns tbody tr.curve td{height:200px}
.patterns td.pct{font-size:24px;font-weight:600;color:var(--ink)}
.patterns td.desc{text-align:left;font-size:14px;line-height:18px;color:var(--ink-soft);padding:0 14px}
.patterns td.group{background:var(--brand);color:var(--white);font-family:"Roboto Condensed",sans-serif;font-weight:700;font-size:28px}
.patterns td.group span{display:inline-block;writing-mode:vertical-rl;transform:rotate(180deg)}
.patterns td.letter-cell{padding:0}
.shape{display:flex;align-items:center;gap:18px;padding:0 20px}
.shape b{font-family:"Roboto Condensed",sans-serif;font-size:30px;color:var(--brand-deep);width:24px}
.patterns tr.total td{height:50px;font-weight:700;font-size:22px;color:var(--brand-deep)}
.patterns tr.total td.total-name{text-align:right;padding-right:20px;font-family:"Roboto Condensed",sans-serif;font-size:24px}
.patterns tr.random td{background:var(--brand-light)}

/* footer */
.footer{position:absolute;left:0;top:4960px;width:1200px;height:204px;background:var(--brand-deep);display:flex;flex-direction:column;align-items:center;justify-content:center;gap:14px;color:var(--white)}
.footer .brand{position:static}
.footer .url{font-size:20px;color:#cfe6f2}
</style>
</head>
<body>

<header class="masthead">
  <svg width="1200" height="320" aria-hidden="true">
    <polygon points="700,0 1200,0 1200,320 900,320" fill="#ffffff" opacity="0.07"/>
    <polygon points="860,0 1200,0 1200,200" fill="#ffffff" opacity="0.08"/>
    <polygon points="0,320 420,320 0,240" fill="#ffffff" opacity="0.06"/>
    <rect x="0" y="300" width="1200" height="20" fill="#0187ac"/>
  </svg>
  <div class="brand"><span class="brand-dot"></span>Gearmont Labs</div>
  <h1 class="title">Reliability<br>Centered<br>Maintenance</h1>
  <div class="subtitle">9 PRINCIPLES OF MODERN MAINTENANCE</div>
</header>

<h2 class="section-title" style="top:335px">History of Reliability Centered Maintenance</h2>

<div class="gen-link" style="left:350px;width:150px"></div>
<div class="gen-link" style="left:730px;width:120px"></div>

<div class="gen" style="left:50px">
  <div class="gen-label">1<sup>st</sup> Generation</div>
  <div class="gen-box">Fix It<br>When It Breaks</div>
  <p class="gen-text">This made equipment reliable and easy to repair. And most plants operated without any preventive maintenance in place.</p>
</div>
<div class="gen" style="left:450px">
  <div class="gen-label">2<sup>nd</sup> Generation</div>
  <div class="gen-box">During<br>World War II</div>
  <p class="gen-text">Fixed interval overhauls or replacements to prevent failures became the norm.</p>
</div>
<div class="gen" style="left:830px">
  <div class="gen-label">3<sup>rd</sup> Generation</div>
  <div class="gen-box">More Maintenance,<br>More Failures</div>
  <p class="gen-text">Replacing components before they reached that age would thus prevent failure.</p>
</div>

<h2 class="section-title" style="top:666px">More Maintenance, More Failures</h2>

<div class="spine"></div>

<div class="node" style="top:735px"></div>
<div class="event left" style="top:722px"><div class="year">1950</div><p>By the 1950's more and more complex machines were in use across almost all industries. Industry as a whole had come to depend on machines.</p></div>

<div class="node" style="top:780px"></div>
<div class="event right" style="top:767px"><div class="year">1958</div><p>After World War II air travel became widely accessible. And passenger numbers grew fast. By 1958 the Civil Flight Safety Office (CFSO) had become concerned about reliability. And passenger safety.</p></div>

<div class="node" style="top:880px"></div>
<div class="event left" style="top:867px"><div class="year">1960</div><p>During the 1960's the airlines and the CFSO established a joint task force to find out what was going on. After analysing 12 years of data the task force concluded that overhauls had little or no effect on overall reliability or safety.</p></div>

<div class="node" style="top:955px"></div>
<div class="event right" style="top:942px"><div class="year">1968</div><p>The first guideline titled "Aircraft Upkeep Planning Guide" came out in 1968. The guide is often referred to as AUG-1 and was specifically written for the Aerodyne 583-240.</p></div>

<div class="node" style="top:1055px"></div>
<div class="event left" style="top:1042px"><div class="year">1970</div><p>The result was AUG-2, released in 1970 titled "Fleet Upkeep Program Design".</p></div>

<div class="node" style="top:1120px"></div>
<div class="event right" style="top:1107px"><div class="year">1974</div><p>In 1974 the defence ministry asked Northwind Airlines to write a report on the processes used to write reliable maintenance programs for civilian aircraft. And in 1978 Ellis Varden and Marcus Quill published their report. It was titled "Reliability Centered Maintenance".</p></div>

<div class="node" style="top:1200px"></div>
<div class="event left" style="top:1187px"><div class="year">1990</div><p>Owen Taskell published his book Asset Care Fundamentals in the 1990's introducing Reliability Centered Maintenance concepts to industry at large.</p></div>

<section class="compare">
  <p class="lead" style="top:28px">The move to 3rd Generation or Reliability Centered Maintenance as outlined AUG-1 and AUG-2 was dramatic.</p>
  <div class="plane-box" style="left:110px">
    <h3>QX-7</h3>
    <p>Used traditional maintenance schedule. It required the overhaul of 339 components and called for more than 4,000,000 labour hours before reaching 20,000 operating hours.</p>
  </div>
  <div class="vs">VS</div>
  <div class="plane-box" style="left:670px">
    <h3>583-240</h3>
    <p>The maintenance schedule for the 583-240 developed using AUG-1 required just 66,000 labour hours before reaching the same 20,000 operating hours!</p>
  </div>
  <p class="lead" style="top:318px;font-weight:500;font-size:21px;line-height:29px">Another interesting comparison is to compare the number of items requiring fixed-time overhauls. The maintenance for the QX-10 was developed using AUG-2 and required the overhaul of just 7 items versus the 339 on the QX-7.</p>
  <p class="lead" style="top:418px;font-weight:500;font-size:21px">And both the QX-10 and 583-240 were larger and more complex than the QX-7.</p>
</section>

<section class="wheel">
  <svg class="abs" style="left:0;top:0" width="1200" height="460" aria-hidden="true">
    <circle cx="600" cy="230" r="150" fill="none" stroke="#0187ac" stroke-width="16" stroke-dasharray="60 18"/>
    <circle cx="600" cy="230" r="128" fill="none" stroke="#c9d3da" stroke-width="2"/>
    <g stroke="#c9d3da" stroke-width="2">
      <line x1="445" y1="52" x2="510" y2="110"/>
      <line x1="445" y1="136" x2="470" y2="150"/>
      <line x1="445" y1="220" x2="450" y2="220"/>
      <line x1="445" y1="304" x2="468" y2="300"/>
      <line x1="445" y1="400" x2="505" y2="350"/>
      <line x1="755" y1="62" x2="690" y2="110"/>
      <line x1="755" y1="165" x2="740" y2="170"/>
      <line x1="755" y1="268" x2="745" y2="268"/>
      <line x1="755" y1="380" x2="700" y2="345"/>
    </g>
  </svg>
  <div class="tag left" style="top:26px">Accept<br>Failures<span class="num">#1</span></div>
  <div class="tag left" style="top:110px">Most Failures Are Not<br>Age Related<span class="num">#2</span></div>
  <div class="tag left" style="top:194px">Some Failures Matter<br>More Than Others<span class="num">#3</span></div>
  <div class="tag left" style="top:278px">Parts Might Wear Out.<br>But Your Equipment<br>Breaks Down<span class="num">#4</span></div>
  <div class="tag left" style="top:374px">Hidden Failures Must<br>Be Found<span class="num">#5</span></div>
  <div class="hub">9 Principles<br>of Modern<br>Maintenance</div>
  <div class="tag right" style="top:36px"><span class="num">#6</span>Identical Equipment<br>Does Not Mean<br>Identical Maintenance</div>
  <div class="tag right" style="top:140px"><span class="num">#7</span>"You Can't Maintain<br>Your Way To<br>Reliability"</div>
  <div class="tag right" style="top:242px"><span class="num">#8</span>Good Maintenance<br>Programs Don't<br>Waste Your<br>Resources</div>
  <div class="tag right" style="top:354px"><span class="num">#9</span>Good Maintenance<br>Programs Become<br>Better Maintenance<br>Programs</div>
</section>

<div class="section-rule" style="top:2316px"></div>

<div class="detail" style="left:70px;top:2345px"><h4><span>#1</span>Accept Failures</h4><p>Not all failures can be prevented by maintenance. Some failures are the result of events outside our control. Think lightning strikes or flooding. For events like these, more or better maintenance makes no difference.</p></div>
<div class="detail" style="left:70px;top:2505px"><h4><span>#2</span>Most Failures Are Not Age Related</h4><p>As explained above the research by the airline industry has shown that 70% – 90% of failure modes are not age related. Instead, for most failure modes the likelihood of occurrence is random. Later research by the navy and others found very similar results.</p></div>
<div class="detail" style="left:70px;top:2680px"><h4><span>#3</span>Some Failures Matter More Than Others</h4><p>Focusing maintenance cost in return for a benefit in improved safety and reliability. And so with all good investments the benefit should outweigh the required investment.</p></div>
<div class="detail" style="left:70px;top:2835px"><h4><span>#4</span>Parts Might Wear Out, But Your Equipment Breaks Down</h4><p>We know the typical wear-out age for a component; we can schedule a time-based task to replace it before failure.</p></div>
<div class="detail" style="left:70px;top:2990px"><h4><span>#5</span>Hidden Failures Must Be Found</h4><p>Hidden failures are failures that remain undetected during normal operation. They only become evident when you need the item to work, so find them on demand.</p></div>

<div class="detail" style="left:630px;top:2345px"><h4><span>#6</span>Identical Equipment Does Not Mean Identical Maintenance</h4><p>The classic example is two exactly the same pumps in a duty. Both pumps process the exact same fluid under the same operating conditions. But Pump A is the duty pump, and Pump B is the standby pump, so each needs its own plan.</p></div>
<div class="detail" style="left:630px;top:2545px"><h4><span>#7</span>"You Can't Maintain Your Way To Reliability"</h4><p>If the equipment's inherent reliability or performance is poor, doing more maintenance will not help. No amount of maintenance can raise the inherent reliability of a design.</p></div>
<div class="detail" style="left:630px;top:2725px"><h4><span>#8</span>Good Maintenance Programs Don't Waste Your Resources</h4><p>As maintainers we should be very careful about maintaining to design capabilities. Instead, in most cases we should maintain our equipment to deliver its operating requirements.</p></div>
<div class="detail" style="left:630px;top:2910px"><h4><span>#9</span>Good Maintenance Programs Become Better Maintenance Programs</h4><p>The most effective maintenance programs are dynamic. They are changing and improving continuously, always making better use of our resources and becoming more effective at preventing those failures that matter to our business.</p></div>

<p class="footnote">* This research is summarised in the six different failure patterns shown below:</p>
<h2 class="table-title">Failure Patterns &amp; Distributions</h2>

<table class="patterns">
  <colgroup><col style="width:70px"><col style="width:290px"><col style="width:95px"><col style="width:95px"><col style="width:95px"><col style="width:95px"><col style="width:300px"></colgroup>
  <thead>
    <tr><th rowspan="2"></th><th rowspan="2">Failure Pattern</th><th colspan="4">Distribution</th><th rowspan="2">Description</th></tr>
    <tr class="src"><th>NWL<br>1968</th><th>Bramberg<br>1973</th><th>FLT<br>1982</th><th>SUBMAINT<br>2001</th></tr>
  </thead>
  <tbody>
    <tr class="curve">
      <td class="group" rowspan="3"><span>Age Related</span></td>
      <td class="letter-cell"><div class="shape"><b>A</b><svg width="210" height="130" viewBox="0 0 240 140" aria-hidden="true"><path d="M6 4 V134 H236" fill="none" stroke="#9aa7b0" stroke-width="3"/><path d="M12 22 Q 26 96 54 100 L 180 100 Q 214 98 230 22" fill="none" stroke="#0187ac" stroke-width="6"/></svg></div></td>
      <td class="pct">4%</td><td class="pct">3%</td><td class="pct">3%</td><td class="pct">2%</td>
      <td class="desc">An initial failure period, followed by the main lifespan of the item, which shows a constant probability of failure. This is followed by a wear-out zone in which the probability of failure increases dramatically.</td>
    </tr>
    <tr class="curve">
      <td class="letter-cell"><div class="shape"><b>B</b><svg width="210" height="130" viewBox="0 0 240 140" aria-hidden="true"><path d="M6 4 V134 H236" fill="none" stroke="#9aa7b0" stroke-width="3"/><path d="M12 100 L 172 100 Q 212 98 230 22" fill="none" stroke="#0187ac" stroke-width="6"/></svg></div></td>
      <td class="pct">2%</td><td class="pct">1%</td><td class="pct">17%</td><td class="pct">10%</td>
      <td class="desc">As "A" but without the initial early failure period.</td>
    </tr>
    <tr class="curve">
      <td class="letter-cell"><div class="shape"><b>C</b><svg width="210" height="130" viewBox="0 0 240 140" aria-hidden="true"><path d="M6 4 V134 H236" fill="none" stroke="#9aa7b0" stroke-width="3"/><path d="M12 112 L 230 40" fill="none" stroke="#0187ac" stroke-width="6"/></svg></div></td>
      <td class="pct">5%</td><td class="pct">4%</td><td class="pct">3%</td><td class="pct">17%</td>
      <td class="desc">The probability of failure increases gradually, but there is no clearly identifiable wear-out lifespan of the equipment.</td>
    </tr>
    <tr class="curve">
      <td class="group" rowspan="3"><span>Random</span></td>
      <td class="letter-cell"><div class="shape"><b>D</b><svg width="210" height="130" viewBox="0 0 240 140" aria-hidden="true"><path d="M6 4 V134 H236" fill="none" stroke="#9aa7b0" stroke-width="3"/><path d="M12 122 Q 40 82 72 80 L 230 80" fill="none" stroke="#0187ac" stroke-width="6"/></svg></div></td>
      <td class="pct">7%</td><td class="pct">11%</td><td class="pct">6%</td><td class="pct">9%</td>
      <td class="desc">The equipment is satisfactory when new, but the failure probability increases rapidly up to a level, which remains constant.</td>
    </tr>
    <tr class="curve">
      <td class="letter-cell"><div class="shape"><b>E</b><svg width="210" height="130" viewBox="0 0 240 140" aria-hidden="true"><path d="M6 4 V134 H236" fill="none" stroke="#9aa7b0" stroke-width="3"/><path d="M12 86 L 230 86" fill="none" stroke="#0187ac" stroke-width="6"/></svg></div></td>
      <td class="pct">14%</td><td class="pct">15%</td><td class="pct">42%</td><td class="pct">56%</td>
      <td class="desc">The type of equipment shows a random failure pattern and again has no identifiable lifespan.</td>
    </tr>
    <tr class="curve">
      <td class="letter-cell"><div class="shape"><b>F</b><svg width="210" height="130" viewBox="0 0 240 140" aria-hidden="true"><path d="M6 4 V134 H236" fill="none" stroke="#9aa7b0" stroke-width="3"/><path d="M12 20 Q 22 92 54 96 L 230 96" fill="none" stroke="#0187ac" stroke-width="6"/></svg></div></td>
      <td class="pct">68%</td><td class="pct">66%</td><td class="pct">29%</td><td class="pct">6%</td>
      <td class="desc">A high infant mortality is superseded by a rapid drop in failure probability, which then remains constant or increases very gradually.</td>
    </tr>
    <tr class="total">
      <td class="total-name" colspan="2">Age Related</td>
      <td>11%</td><td>8%</td><td>23%</td><td>29%</td><td></td>
    </tr>
    <tr class="total random">
      <td class="total-name" colspan="2">Random</td>
      <td>89%</td><td>92%</td><td>77%</td><td>71%</td><td></td>
    </tr>
  </tbody>
</table>

<footer class="footer">
  <div class="brand"><span class="brand-dot"></span>Gearmont Labs</div>
  <div class="url">www.gearmontlabs.com</div>
</footer>

</body>
</html>
```